DJ Equipment Rental (business card/packet folder/stationary)

Designers:
The address will not longer be included in any of these designs. Thanks!

Attention designers,
It was brought to my attention that my brief was too broad and VERY confusing :/. I truly apologize.

This is what I need:
*Front and back business cards.
*A packet folder (front and back) (The size big enough to hold the 8x11 sheets)
I really don't know he size.

*Letter head

I needs to be professional, elegant, and it needs to stand out. Corporate like.

Colors:
Deep Red, Black, Deep blue . Also, follow color scheme of current logo but get creative.

Company: Vinyl Crate Hire Co
Phone: 918.555.0142
Email: Rentals@VinylCrateHireCo.example
Web: www.VinylCrateHireCo.example (under construction)
Address: 4826 W. Alder Lane, Tulsa, OK 74100
Logo: Provided

Project Deadline Extended
Reason: Due to my poor explanation and description of the project, I'm extending the due date of this project.

Target Market(s)

This folder will have my information as a business and it will serve as a marketing material. The audience range age is 18-43.

Industry/Entity Type

Business

Requirements
Must have
• Follow the color scheme provide in the logo.

```html
<!DOCTYPE html>
<html lang="en">
<head>
<meta charset="utf-8">
<title>Vinyl Crate Hire Co — Business Card</title>
<link href="https://fonts.googleapis.com/css2?family=Ubuntu:ital,wght@0,400;0,500;0,700;1,700&display=swap" rel="stylesheet">
<style>
  :root {
    --stage: #e9e6e4;
    --card: #0b0b0b;
    --ink: #f2f2f2;
    --brand-red: #d8412f;
    --amber: #d9a43a;
    --red: #c8302f;
    --sand: #c9a36a;
    --sky: #5fa6c9;
    --teal: #69b2b0;
    --shadow: rgba(0,0,0,0.35);
  }
  * { margin: 0; padding: 0; box-sizing: border-box; }
  html, body {
    width: 1200px; height: 968px; overflow: hidden;
    background: var(--stage);
    font-family: "Ubuntu", Arial, sans-serif;
  }
  .stage { position: relative; width: 1200px; height: 968px; }
  .card {
    position: absolute; left: 280px;
    width: 640px; height: 366px;
    background: var(--card);
    border-radius: 26px;
    box-shadow: 0 14px 30px var(--shadow);
    overflow: hidden;
    color: var(--ink);
  }
  .card--back { top: 70px; }
  .card--front { top: 530px; }

  .card__web {
    position: absolute; top: 78px; right: 70px;
    font-weight: 700; font-style: italic;
    font-size: 17px; letter-spacing: 0.8px;
  }
  .level-band {
    position: absolute; left: 0; right: 0; bottom: 30px;
    height: 136px;
    background: linear-gradient(90deg, var(--amber) 0%, var(--red) 35%, var(--red) 55%, var(--sand) 72%, var(--sky) 85%, var(--teal) 100%);
    opacity: 0.85;
  }

  .brand {
    position: absolute; top: 58px; left: 0; right: 0;
    display: flex; align-items: center; justify-content: center; gap: 14px;
  }
  .brand__mark { width: 18px; height: 18px; background: var(--brand-red); }
  .brand__name {
    font-weight: 700; font-size: 40px; color: var(--brand-red);
    letter-spacing: 1px;
  }
  .contact {
    position: absolute; top: 150px; left: 0; right: 0;
    list-style: none; text-align: center;
    font-size: 18px; font-weight: 500;
  }
  .contact__item { margin-bottom: 10px; }
  .contact__icon {
    display: block; margin: 0 auto 4px;
    width: 18px; height: 16px;
  }
</style>
</head>
<body>
<main class="stage">

  <section class="card card--back" aria-label="Card back">
    <p class="card__web">www.VinylCrateHireCo.example</p>
    <div class="level-band" role="img" aria-label="Multicolour sound level graphic in amber, red and blue tones"></div>
  </section>

  <section class="card card--front" aria-label="Card front">
    <div class="brand">
      <span class="brand__mark"></span>
      <span class="brand__name">Vinyl Crate Hire Co</span>
    </div>
    <ul class="contact">
      <li class="contact__item">
        <svg class="contact__icon" viewBox="0 0 18 16" aria-hidden="true">
          <circle cx="9" cy="8" r="7" fill="none" stroke="#f2f2f2" stroke-width="1.4"/>
          <path d="M6.5 4.5 Q5.5 8 7.5 11 L9 10 L8 8 L8.8 6.5 Z" fill="#f2f2f2"/>
        </svg>
        918.555.0142
      </li>
      <li class="contact__item">
        <svg class="contact__icon" viewBox="0 0 18 16" aria-hidden="true">
          <rect x="1.5" y="3" width="15" height="10" fill="none" stroke="#f2f2f2" stroke-width="1.4"/>
          <path d="M1.5 3 L9 9 L16.5 3" fill="none" stroke="#f2f2f2" stroke-width="1.4"/>
        </svg>
        Rentals@VinylCrateHireCo.example
      </li>
      <li class="contact__item">
        <svg class="contact__icon" viewBox="0 0 18 16" aria-hidden="true">
          <path d="M2 8 L9 2 L16 8 M4 7 V14 H14 V7 M7.5 14 V10 H10.5 V14" fill="none" stroke="#f2f2f2" stroke-width="1.4"/>
        </svg>
        4826 W. Alder Lane, Tulsa, OK 74100
      </li>
    </ul>
  </section>

</main>
</body>
</html>
```